Menubook for a 2star restaurant

Hey,
We are looking for a new menu for a 2 star restaurant in Belgium. They want a clean, abstract, with small light accents of gold, copper. The format will be 21 cm by 21 cm. and the booklet will have 4 printable sides inc front & back. Only the logo on the front. The wine list will be separate so it should not be included in the design. "Bites" - "voorgerechten" - "hoofdgerechten" & "nagerechten" must be copied.

Industry/Entity Type

Restaurant

Requirements
Must have
• Clean look
Nice to have
• touches of gold

```html
<!DOCTYPE html>
<html lang="nl">
<head>
<meta charset="utf-8">
<title>Menu – Bites &amp; Voorgerechten</title>
<link rel="stylesheet" href="https://fonts.googleapis.com/css2?family=Arvo:ital,wght@0,400;0,700;1,400&display=swap">
<style>
  :root {
    --gold: #dcb71f;
    --ink: #161411;
    --title: #eaf6e2;
    --band: #0b0b0b;
  }
  html, body { margin: 0; padding: 0; overflow: hidden; background: var(--band); }
  .menu-page {
    position: relative; width: 1200px; height: 1200px; overflow: hidden;
    background: var(--band); font-family: "Arvo", "Rockwell", serif; color: var(--ink);
  }
  .photo { position: absolute; left: 0; width: 1200px; }
  .photo--oysters {
    top: 0; height: 571px;
    background:
      radial-gradient(ellipse 380px 220px at 850px 270px, #d9d6cc 0%, #a9a59a 40%, transparent 75%),
      radial-gradient(ellipse 300px 160px at 1050px 520px, #8d8a84 0%, transparent 70%),
      linear-gradient(120deg, #3a3833 0%, #6f6b63 45%, #cfcfcb 80%, #efefec 100%);
  }
  .photo--platter {
    top: 597px; height: 603px;
    background:
      radial-gradient(ellipse 180px 260px at 140px 220px, #cdb08a 0%, transparent 70%),
      radial-gradient(ellipse 140px 120px at 330px 530px, #a8232a 0%, transparent 70%),
      radial-gradient(ellipse 200px 120px at 860px 560px, #4d5a2a 0%, transparent 75%),
      linear-gradient(160deg, #4a2420 0%, #3a1b18 50%, #2a1613 100%);
  }
  .panel { position: absolute; background: var(--gold); }
  .panel--bites { left: 0; top: 83px; width: 572px; height: 488px; }
  .panel--starters { left: 628px; top: 597px; width: 572px; height: 488px; }

  .section-title {
    position: absolute; margin: 0; font-weight: 400; color: var(--title);
    line-height: 1; letter-spacing: 0.5px;
  }
  .panel--bites .section-title { left: 67px; top: 34px; font-size: 45px; }
  .panel--starters .section-title { left: 28px; top: 97px; font-size: 48px; }

  .line {
    position: absolute; height: 24px; line-height: 24px; font-size: 18.5px; white-space: nowrap;
  }
  .dish { font-weight: 400; text-transform: none; }
  .note { font-style: italic; }
  .price { position: absolute; text-align: right; height: 24px; line-height: 24px; font-size: 18.5px; }
</style>
</head>
<body>
<main class="menu-page">
  <div class="photo photo--oysters" role="img" aria-label="Close-up photo of fresh oysters on a white plate"></div>
  <div class="photo photo--platter" role="img" aria-label="Photo of an antipasti platter with crackers, cheese, stuffed peppers, pesto and olives"></div>

  <section class="panel panel--bites">
    <h2 class="section-title">BITES</h2>
    <div class="line dish" style="left:67px; top:99px">OESTER DELAVAUX (1st)</div>
    <div class="price" style="right:55px; top:99px">9</div>
    <div class="line note" style="left:67px; top:147px">jalapeño | komkommer | ajo blanco</div>
    <div class="line note" style="left:67px; top:195px">supplement kaviaar 5gr (+ €18)</div>
    <div class="line dish" style="left:67px; top:244px">‘nduja RISOTTO CROQUETTES (2st)</div>
    <div class="price" style="right:55px; top:244px">9</div>
    <div class="line dish" style="left:67px; top:292px">CHARCUTERIE</div>
    <div class="price" style="right:55px; top:292px">15</div>
    <div class="line note" style="left:67px; top:341px">cornichon | olijven</div>
    <div class="line dish" style="left:67px; top:389px">KOUDE AMANDEL-KNOFLOOK ZUPPA</div>
    <div class="price" style="right:55px; top:389px">14</div>
    <div class="line note" style="left:67px; top:437px">fregola | kreeft</div>
  </section>

  <section class="panel panel--starters">
    <h2 class="section-title">VOORGERECHTEN</h2>
    <div class="line dish" style="left:28px; top:167px">ANTIPASTI *</div>
    <div class="price" style="right:75px; top:167px">35 p.p.</div>
    <div class="line dish" style="left:28px; top:216px">PIZZETTA AMARO</div>
    <div class="line note" style="left:28px; top:264px">met 1/2 kreeft | doperwt |</div>
    <div class="line note" style="left:28px; top:312px">basilicum | courgette</div>
    <div class="price" style="right:125px; top:312px">37</div>
    <div class="line note" style="left:28px; top:361px">ook vegetarisch te bestellen</div>
    <div class="price" style="right:125px; top:361px">32</div>
  </section>
</main>
</body>
</html>
```